The Lindenmoor Compass Book

Cover Design for my first book. The book is for elementary school principals who are unhappy and are considering a career change but are afraid to leave. I teach them how to develop emotional fitness and resiliency through thought management so that they can decide whether to stay or leave their position from a place of empowerment. I've attached my podcast artwork for your reference. My publisher suggested not having me on the cover which is fine. I just thought it might be helpful.

Target Market(s)

Elementary School Principals

Industry/Entity Type

Education

Logo Text

The Lindenmoor Compass

Font styles to use
Serif
Sans Serif

Colors
34a6d7
33b8a4
3276b5

Requirements
Must have
• Title, Author name, photo or artwork that captures the essence of the book

```html
<!DOCTYPE html>
<html lang="en">
<head>
<meta charset="utf-8">
<title>The Lindenmoor Compass — Book Cover</title>
<link rel="stylesheet" href="https://fonts.googleapis.com/css2?family=Playfair+Display:wght@400;700;900&display=swap">
<style>
  :root {
    --cover-white: #ffffff;
    --brand-blue: #3276b5;
    --case-blue: #2f6fb0;
    --case-shadow: #1f4f86;
    --building-cream: #efe6cf;
    --building-gold: #cdb86a;
  }
  html, body {
    margin: 0;
    padding: 0;
    width: 848px;
    height: 1200px;
    overflow: hidden;
    background: var(--cover-white);
  }
  .cover {
    position: relative;
    width: 848px;
    height: 1200px;
    background: var(--cover-white);
    font-family: "Playfair Display", Georgia, serif;
    overflow: hidden;
  }
  .author {
    position: absolute;
    top: 30px;
    left: 0;
    width: 100%;
    text-align: center;
    margin: 0;
    font-size: 40px;
    font-weight: 400;
    letter-spacing: 0.5px;
    color: var(--brand-blue);
    line-height: 1.2;
  }
  .author .surname { font-weight: 700; }
  .cover-art {
    position: absolute;
    left: 112px;
    top: 184px;
    width: 588px;
    height: 596px;
    border-radius: 28px;
    background:
      radial-gradient(ellipse at 50% 62%, var(--building-cream) 0%, var(--building-gold) 22%, transparent 40%),
      linear-gradient(160deg, var(--case-blue) 0%, var(--brand-blue) 55%, var(--case-shadow) 100%);
  }
  .title-band {
    position: absolute;
    left: 0;
    top: 870px;
    width: 848px;
    height: 330px;
    background: var(--brand-blue);
    color: var(--cover-white);
  }
  .title { margin: 0; font-weight: 400; }
  .title span { position: absolute; line-height: 1; }
  .title .lead {
    left: 94px;
    top: 44px;
    font-size: 58px;
    font-weight: 400;
  }
  .title .main {
    left: 94px;
    top: 106px;
    font-size: 80px;
    font-weight: 900;
    letter-spacing: -1px;
  }
  .title .tail {
    right: 112px;
    top: 202px;
    font-size: 60px;
    font-weight: 400;
  }
</style>
</head>
<body>
  <main class="cover">
    <p class="author">MARIANNE HOLT <span class="surname">DELANEY</span></p>
    <div class="cover-art" role="img" aria-label="Illustration of an open blue briefcase holding a miniature school building complex"></div>
    <section class="title-band">
      <h1 class="title">
        <span class="lead">THE</span>
        <span class="main">LINDENMOOR</span>
        <span class="tail">COMPASS</span>
      </h1>
    </section>
  </main>
</body>
</html>
```